Business Card for Graphic Design Firm

This project is for a new graphic design firm based in New Jersey called Velmoth. We outsource graphic design and marketing jobs. We want to communicate that this is a professional company but it as well creative and artistic. This card may be used as a horizontal double sided paper card or a vertical single sided translucent card so feel free to submit designs in whichever format or both.
Updates

Reason: Extending the deadline because I'm not exactly satisfied with the designs so far.

Please view the updated project brief

Target Market(s)

Adults aged 25-60

Industry/Entity Type

Graphic Design

Font styles to use
Serif
Sans Serif

Requirements
Nice to have
• Maybe a triangular pattern around the edges similar to our logo

```html
<!DOCTYPE html>
<html lang="en">
<head>
<meta charset="utf-8">
<title>Velmoth — Business Card</title>
<link rel="stylesheet" href="https://fonts.googleapis.com/css2?family=Michroma&family=Open+Sans:wght@300;400;600&display=swap">
<style>
  :root {
    --stage: #e9e7e3;
    --paper: #ffffff;
    --paper-shade: #f3f3f3;
    --ink: #6d6f72;
    --ink-soft: #8b8d90;
    --teal: #1fa9c4;
    --teal-deep: #1789a6;
    --sky: #9fd3e3;
    --slate: #7e8a90;
    --yellow: #f7cf1d;
    --amber: #f0a52a;
  }
  * { box-sizing: border-box; margin: 0; padding: 0; }
  html, body { width: 1200px; height: 1023px; overflow: hidden; }
  body {
    background: var(--stage);
    font-family: "Open Sans", Arial, sans-serif;
    color: var(--ink);
    position: relative;
  }
  .card {
    position: absolute;
    left: 250px;
    width: 700px;
    height: 400px;
    background: linear-gradient(160deg, var(--paper) 55%, var(--paper-shade));
    box-shadow: 0 6px 18px rgba(0,0,0,.18);
    overflow: hidden;
  }
  .card--front { top: 70px; }
  .card--back { top: 553px; }

  .front__identity { position: absolute; left: 60px; top: 56px; }
  .front__name {
    font-family: "Michroma", "Open Sans", sans-serif;
    font-size: 22px;
    letter-spacing: 1px;
    color: var(--ink);
    text-transform: uppercase;
  }
  .front__role { font-size: 13px; color: var(--ink-soft); margin-top: 4px; }
  .contact-list { list-style: none; margin-top: 22px; }
  .contact-list li {
    display: flex; align-items: center; gap: 10px;
    font-size: 15px; color: var(--ink-soft); line-height: 26px;
  }
  .contact-icon { width: 14px; height: 14px; flex: none; }
  .front__address {
    position: absolute; right: 50px; top: 150px;
    text-align: right; font-size: 15px; line-height: 24px; color: var(--ink-soft);
  }
  .front__band { position: absolute; left: 0; bottom: 0; width: 700px; height: 190px; }

  .back__corners { position: absolute; inset: 0; width: 700px; height: 400px; }
  .back__brand {
    position: absolute; left: 0; right: 0; top: 168px;
    display: flex; justify-content: center; align-items: center; gap: 18px;
  }
  .back__mark { width: 26px; height: 26px; background: var(--amber); }
  .back__name {
    font-family: "Open Sans", Arial, sans-serif;
    font-weight: 300; font-size: 54px; letter-spacing: 10px;
    color: var(--ink-soft); text-transform: uppercase;
  }
</style>
</head>
<body>

<section class="card card--front" aria-label="Business card front">
  <div class="front__identity">
    <h1 class="front__name">Dario Fenwick</h1>
    <p class="front__role">Director</p>
    <ul class="contact-list">
      <li>
        <svg class="contact-icon" viewBox="0 0 14 14" aria-hidden="true">
          <rect width="14" height="14" rx="2" fill="var(--amber)"/>
          <path d="M4 3.5 L5.5 3.5 L6.2 5.5 L5.3 6.3 Q6.2 8 7.7 8.7 L8.5 7.8 L10.5 8.5 L10.5 10 Q6 10.5 4 3.5Z" fill="#fff"/>
        </svg>555-010-2468</li>
      <li>
        <svg class="contact-icon" viewBox="0 0 14 14" aria-hidden="true">
          <rect width="14" height="14" rx="2" fill="var(--amber)"/>
          <circle cx="7" cy="7" r="4" fill="none" stroke="#fff" stroke-width="1"/>
          <path d="M3 7 H11 M7 3 Q4.8 7 7 11 M7 3 Q9.2 7 7 11" fill="none" stroke="#fff" stroke-width=".8"/>
        </svg>www.velmothstudio.com</li>
      <li>
        <svg class="contact-icon" viewBox="0 0 14 14" aria-hidden="true">
          <rect width="14" height="14" rx="2" fill="var(--amber)"/>
          <rect x="3" y="4.2" width="8" height="5.6" fill="none" stroke="#fff" stroke-width="1"/>
          <path d="M3 4.2 L7 7.4 L11 4.2" fill="none" stroke="#fff" stroke-width="1"/>
        </svg>hello@velmothstudio.com</li>
    </ul>
  </div>
  <address class="front__address" style="font-style:normal">
    18 Orchard Lane Westfield<br>NJ 07090
  </address>
  <svg class="front__band" viewBox="0 0 700 190" aria-hidden="true">
    <defs>
      <linearGradient id="warmBand" x1="0" y1="1" x2="1" y2="0">
        <stop offset="0" stop-color="var(--yellow)"/>
        <stop offset="1" stop-color="var(--amber)"/>
      </linearGradient>
    </defs>
    <polygon points="0,40 210,40 300,190 0,190" fill="var(--teal)"/>
    <polygon points="0,40 90,40 0,110" fill="var(--teal-deep)" opacity=".7"/>
    <polygon points="330,40 700,40 700,190 420,190" fill="url(#warmBand)"/>
    <rect x="250" y="40" width="60" height="150" fill="var(--paper)" transform="skewX(30) translate(-70 0)"/>
  </svg>
</section>

<section class="card card--back" aria-label="Business card back">
  <svg class="back__corners" viewBox="0 0 700 400" aria-hidden="true">
    <polygon points="0,0 170,0 0,110" fill="var(--sky)" opacity=".35"/>
    <polygon points="0,110 60,110 0,170" fill="var(--amber)" opacity=".12"/>
    <polygon points="700,400 470,400 700,260" fill="var(--sky)" opacity=".35"/>
    <polygon points="700,110 600,200 700,260" fill="var(--amber)" opacity=".12"/>
  </svg>
  <div class="back__brand">
    <span class="back__mark" aria-hidden="true"></span>
    <h2 class="back__name">Velmoth</h2>
  </div>
</section>

</body>
</html>
```